Calder Pizza - Takeout Menu Design

We are looking for a takeout menu design.
We are looking for a( 5" x 8.5" DOUBLE SIDED) flyer with our available pizza flavors
Must be easy to ready and not "busy"

Must include our logo (attached)
website: www.calderpizza.ca
address:
Fenwick Ridge Plaza
417, 318 9 Avenue SW
and the following details:
Visit our website for our complete appetizer, pasta, salad and catering menu.

Winner of this contest will also be offered to create a few print designs via printhive.

Please do not hesitate to ask any questions.

Target Market(s)

Business / Office clientele

Industry/Entity Type

Pizza place / specializing in corporate orders

Requirements
Must have
• Easy to read
Should not have
• Can not be busy or cluttered

```html
<!DOCTYPE html>
<html lang="en">
<head>
<meta charset="utf-8">
<title>Calder Pizza – Takeout Menu</title>
<link href="https://fonts.googleapis.com/css2?family=Lexend:wght@300;400;600;700&family=Titan+One&family=Anton&family=Poppins:wght@400;500&display=swap" rel="stylesheet">
<style>
:root{
  --page:#e8e8e9;
  --brown:#6a2e14;
  --brown-deep:#4a1c0b;
  --brown-dark:#2c120a;
  --cream:#ffffff;
  --label:#8b2b10;
  --yellow:#f7c21a;
  --orange:#f1541f;
  --red:#e8302a;
  --rule:rgba(255,255,255,.35);
}
*{box-sizing:border-box;margin:0;padding:0}
html,body{width:1200px;height:800px;overflow:hidden;background:var(--page)}
body{position:relative;font-family:"Poppins",sans-serif;color:var(--cream)}

/* ---------- front side ---------- */
.front{position:absolute;left:148px;top:53px;width:405px;height:690px;overflow:hidden;background:var(--brown-dark)}
.front-scene{position:absolute;inset:0;background:linear-gradient(180deg,#3a1d14 0%,#5a2a18 45%,#3b1a10 75%,#6b2a18 100%)}
.front-pizzas{position:absolute;left:38px;top:255px;width:335px;height:330px;border-radius:50%;
  background:radial-gradient(circle at 50% 55%,#d9722f 0%,#c2552a 45%,#a7682d 70%,rgba(120,60,30,0) 72%)}
.title-card{position:absolute;left:35px;top:42px;width:335px;height:200px;border:1.5px dashed var(--cream);border-radius:14px;background:rgba(40,30,30,.55);text-align:center}
.brand{margin-top:13px;font-family:"Lexend",sans-serif;font-weight:300;font-size:15px;letter-spacing:.5px;color:var(--cream)}
.headline{margin-top:8px;font-family:"Lexend",sans-serif;font-weight:700;font-size:41px;line-height:1.1;letter-spacing:-.5px}
.tagline{margin-top:18px;font-family:"Titan One",sans-serif;font-size:17px;line-height:1.3;text-transform:uppercase}
.tagline .big{font-size:29px}
.tagline .gold{color:var(--yellow)}
.tagline .fire{color:var(--orange)}
.info-card{position:absolute;left:105px;top:583px;width:210px;height:100px;border:1.5px dashed var(--cream);border-radius:10px;background:rgba(60,30,20,.6);text-align:center;font-family:"Lexend",sans-serif;font-weight:600;font-size:11.5px;line-height:1.25;padding-top:14px}
.info-card p + p{margin-top:8px}

/* ---------- back side ---------- */
.back{position:absolute;left:591px;top:55px;width:405px;height:690px;overflow:hidden;background:var(--brown)}
.card{position:absolute;border:1.3px dashed var(--cream);border-radius:11px;background:var(--brown-deep)}
.logo-card{left:18px;top:16px;width:61px;height:113px;display:flex;align-items:center;justify-content:center}
.logo-card span{writing-mode:vertical-rl;font-family:"Lexend",sans-serif;font-weight:300;font-size:20px;letter-spacing:1px;color:var(--cream)}

.cols{display:grid;grid-template-columns:1fr 30px 32px;align-items:center}
.pill{position:absolute;left:5px;right:5px;top:7px;height:28px;padding:0 5px 0 9px;background:var(--cream);border-radius:14px;color:var(--label);font-family:"Titan One",sans-serif}
.pill .t1{display:block;font-size:6px;letter-spacing:.2px;line-height:1.2}
.pill .t2{display:block;font-size:4.5px;line-height:1.3}
.pill .sz{font-size:5px;text-align:right}
.name{font-family:"Titan One",sans-serif;font-size:6px;letter-spacing:.2px;white-space:nowrap}
.desc{font-size:4.2px;line-height:1.45;margin-top:2px;padding-right:4px;color:#f3e6e0}
.price{font-family:"Titan One",sans-serif;font-size:5.2px;text-align:right;white-space:nowrap}

.top-card{left:89px;top:16px;width:303px;height:113px}
.top-card .pill{padding-right:9px}
.wide{grid-template-columns:1fr 30px 32px 1fr 30px 32px;column-gap:0}
.wide .half2{padding-left:10px}
.top-grid{position:absolute;left:9px;right:14px;top:48px;row-gap:11px}

.list{position:absolute;left:10px;right:10px;display:flex;flex-direction:column}
.item{flex:1;border-bottom:.6px solid var(--rule)}
.item:last-child{border-bottom:none}
.item.stack{display:flex;flex-direction:column;justify-content:center}
.sub{font-size:4.2px;height:10px}

.chicken-card{left:18px;top:138px;width:179px;height:281px}
.veg-card{left:18px;top:427px;width:179px;height:245px}
.meat-card{left:206px;top:138px;width:186px;height:403px}
.note-card{left:206px;top:551px;width:186px;height:121px}
.note{position:absolute;left:18px;top:26px;width:128px;font-family:"Anton",sans-serif;font-size:10.5px;line-height:1.25;color:var(--cream);z-index:2}
.gst{display:block;margin-top:6px;color:var(--red);font-size:9.5px}

.photo{position:absolute;border-radius:50%}
.pizza-top{left:167px;top:116px;width:74px;height:38px;background:radial-gradient(circle,#c0462a 0%,#b55a2e 55%,#d59a5a 100%)}
.pizza-ghost{left:11px;top:338px;width:388px;height:97px;background:radial-gradient(ellipse,rgba(200,90,40,.35) 0%,rgba(120,50,20,0) 70%)}
.pizza-board{left:348px;top:628px;width:62px;height:62px;background:radial-gradient(circle,#d0642f 0%,#b5562a 50%,#8b4a22 100%)}
</style>
</head>
<body>

<section class="front">
  <div class="front-scene" role="img" aria-label="Blurred pizzeria backdrop with glowing embers"></div>
  <div class="front-pizzas photo" role="img" aria-label="Two freshly baked pizzas topped with cheese, beef, olives and peppers"></div>

  <header class="title-card">
    <div class="brand">CALDER PIZZA</div>
    <h1 class="headline">Pizza Paradise</h1>
    <p class="tagline">A pizza made in <span class="big gold">Pizza</span><br><span class="big fire">Heaven</span>, just for you</p>
  </header>

  <footer class="info-card">
    <p>Mon – Fri: 9 AM – 4:30 PM</p>
    <p>www.calderpizza.ca</p>
    <p>Address: Fenwick Ridge Plaza 417,<br>318 9 Avenue SW</p>
  </footer>
</section>

<section class="back">
  <div class="photo pizza-ghost" role="img" aria-label="Faint pizza in the background"></div>

  <div class="card logo-card"><span>CALDER PIZZA</span></div>

  <div class="card top-card">
    <div class="pill cols wide">
      <div><span class="t1">SPECIALTY CHICKEN</span><span class="t2">TAKE-OUT PIZZA</span></div>
      <span class="sz">8"</span><span class="sz">13"</span>
      <span class="half2"></span><span class="sz">8"</span><span class="sz">13"</span>
    </div>
    <div class="top-grid cols wide">
      <span class="name">PEPPERONI MUSHROOM</span><span class="price">$13.99</span><span class="price">$35.95</span>
      <span class="name half2">PEPPERONI</span><span class="price">$13.99</span><span class="price">$35.95</span>
      <span class="name">HAWAIIAN</span><span class="price">$13.99</span><span class="price">$35.95</span>
      <span class="name half2">BEEF + ONION</span><span class="price">$13.99</span><span class="price">$35.95</span>
      <span class="name">CHEESE</span><span class="price">$13.99</span><span class="price">$35.95</span>
      <span class="name half2">BEEF + MUSHROOM</span><span class="price">$13.99</span><span class="price">$35.95</span>
    </div>
  </div>

  <div class="card chicken-card">
    <div class="pill cols"><div><span class="t1">SPECIALTY CHICKEN</span><span class="t2">TAKE-OUT PIZZA</span></div><span class="sz">8"</span><span class="sz">13"</span></div>
    <div class="list" style="top:44px;bottom:6px">
      <div class="item cols"><div><div class="name">BBQ CHICKEN</div><div class="desc">Chicken Breast, Hickory BBQ Sauce &amp; Red Onions.</div></div><span class="price">$13.99</span><span class="price">$33.95</span></div>
      <div class="item cols"><div><div class="name">BBQ CHICKEN PLUS</div><div class="desc">Chicken Breast, Hickory BBQ Sauce, Red Onions &amp; Cilantro</div></div><span class="price">$14.79</span><span class="price">$34.95</span></div>
      <div class="item cols"><div><div class="name">BBQ CHICKEN PLUS</div><div class="desc">Chicken Breast, Hickory BBQ Sauce, Red Onions &amp; Cilantro</div></div><span class="price">$14.79</span><span class="price">$34.95</span></div>
      <div class="item cols"><div><div class="name">GREEK SUPREME</div><div class="desc">Chicken Breast, Feta Cheese, Tomato, Green Pepper, Red Onions &amp; Black Olives</div></div><span class="price">$14.99</span><span class="price">$35.95</span></div>
      <div class="item cols"><div><div class="name">CHICKEN CLUB</div><div class="desc">Chicken Breast, Double Smoked Bacon, Red Onions and Tomatoes</div></div><span class="price">$14.79</span><span class="price">$35.95</span></div>
      <div class="item cols"><div><div class="name">MEDITERRANEAN CHICKEN</div><div class="desc">Seasoned Chicken Breast, Tomatoes, Red Onions and Feta Cheese</div></div><span class="price">$14.79</span><span class="price">$35.95</span></div>
      <div class="item cols"><div><div class="name">SWEET CHILI CHICKEN</div><div class="desc">Chicken Breast, Pineapple, Red Onions &amp; Sweet Chili Sauce</div></div><span class="price">$14.49</span><span class="price">$35.95</span></div>
    </div>
  </div>

  <div class="card veg-card">
    <div class="pill cols"><div><span class="t1">SPECIALTY CHICKEN</span><span class="t2">TAKE-OUT PIZZA</span></div><span class="sz">8"</span><span class="sz">13"</span></div>
    <div class="list" style="top:42px;bottom:6px">
      <div class="item cols"><div><div class="name">ORIGINAL SPINACH</div><div class="desc">Spinach &amp; Feta Cheese</div></div><span class="price">$13.49</span><span class="price">$32.95</span></div>
      <div class="item cols"><div><div class="name">ZEUS</div><div class="desc">Spinach, Feta Cheese and Tomatoes</div></div><span class="price">$13.95</span><span class="price">$33.95</span></div>
      <div class="item cols"><div><div class="name">GREEK</div><div class="desc">Mushrooms, Tomatoes, Green Peppers and Black Olives</div></div><span class="price">$13.99</span><span class="price">$35.95</span></div>
      <div class="item cols"><div><div class="name">VEGETARIAN</div><div class="desc">Mushrooms, Tomatoes, Green Peppers and Black Olives</div></div><span class="price">$13.49</span><span class="price">$32.95</span></div>
      <div class="item cols"><div><div class="name">VEGGIE DELIGHT</div><div class="desc">Mushrooms, Tomatoes, Green Peppers, Black Olives &amp; Onions</div></div><span class="price">$13.99</span><span class="price">$35.95</span></div>
      <div class="item stack" style="flex:2.2">
        <div class="name">DILL PICKLE</div>
        <div class="desc" style="width:110px">Crispy Dill Pickles, Fresh Dill with our cream based garlic sauce. Served with our without bacon</div>
        <div class="sub cols" style="margin-top:3px"><span>Served with bacon</span><span class="price">$13.49</span><span class="price">$35.95</span></div>
        <div class="sub cols"><span>Served without bacon</span><span class="price">$14.49</span><span class="price">$35.95</span></div>
      </div>
    </div>
  </div>

  <div class="card meat-card">
    <div class="pill cols"><div><span class="t1">SPECIALTY NON VEG</span><span class="t2">TAKE-OUT PIZZA</span></div><span class="sz">8"</span><span class="sz">13"</span></div>
    <div class="list" style="top:42px;bottom:6px">
      <div class="item cols"><div><div class="name">ALL MEAT</div><div class="desc">Pepperoni, Beef &amp; Smoked Ham &amp; Bacon</div></div><span class="price">$14.99</span><span class="price">$35.95</span></div>
      <div class="item cols"><div><div class="name">DOUBLE PEPPERONI</div><div class="desc">Loads of Pepperoni</div></div><span class="price">$13.49</span><span class="price">$32.95</span></div>
      <div class="item cols"><div><div class="name">HAWAIIAN HEAT</div><div class="desc">Smoked Ham, Pineapple and Banana Peppers</div></div><span class="price">$13.49</span><span class="price">$32.95</span></div>
      <div class="item cols"><div><div class="name">HOT HONEY PEPPERONI</div><div class="desc">Double Pepperoni and drizzled with Hot</div></div><span class="price">$14.99</span><span class="price">$34.95</span></div>
      <div class="item cols"><div><div class="name">MONTREAL</div><div class="desc">Pepperoni &amp; Double Smoked Bacon</div></div><span class="price">$13.49</span><span class="price">$32.95</span></div>
      <div class="item cols"><div><div class="name">FOUR CHEESE</div><div class="desc">Mozzarella, Feta, Romano and Cheddar Cheese</div></div><span class="price">$13.49</span><span class="price">$32.95</span></div>
      <div class="item cols"><div><div class="name">MONTREAL HEAT</div><div class="desc">Pepperoni, Double Smoked Bacon &amp; Banana Peppers</div></div><span class="price">$13.99</span><span class="price">$32.95</span></div>
      <div class="item cols"><div><div class="name">SUPREME</div><div class="desc">Pepperoni, Mushrooms &amp; Green Peppers</div></div><span class="price">$13.49</span><span class="price">$32.95</span></div>
      <div class="item cols"><div><div class="name">CANADIAN</div><div class="desc">Pepperoni, Mushrooms &amp; Ham</div></div><span class="price">$13.49</span><span class="price">$32.95</span></div>
      <div class="item cols"><div><div class="name">DELUXE</div><div class="desc">Pepperoni, Mushrooms, Ham, Tomatoes, Green Peppers and Red Onions</div></div><span class="price">$14.99</span><span class="price">$34.95</span></div>
      <div class="item cols"><div><div class="name">CALDER SPECIAL</div><div class="desc">Pepperoni, Mushrooms, Ham, Green Peppers and Black Olives</div></div><span class="price">$14.49</span><span class="price">$34.95</span></div>
      <div class="item cols"><div><div class="name">BBQ PULLED PORK</div><div class="desc">Pulled Pork, Red Onions, Red Peppers and Cilantro.</div></div><span class="price">$14.49</span><span class="price">$35.95</span></div>
    </div>
  </div>

  <div class="card note-card">
    <p class="note">All of our pizzas are prepared fresh everyday using only the finest mozzarella blend and ingredients.<span class="gst">GST not included.</span></p>
  </div>

  <div class="photo pizza-top" role="img" aria-label="Whole pepperoni pizza seen from the side"></div>
  <div class="photo pizza-board" role="img" aria-label="Sliced pizza on a wooden serving board"></div>
</section>

</body>
</html>
```